Business Card Design

Business sales of reconditioned / used batteries with mobile delivery and install services. Customers base majority are auto car sales lots and individuals.

Card need to convey quality product reliability and quick prompt professional service.

Card must reflect excellence in customer care and product being offered

Target Market(s)

Auto car lots new and used. Auto repair shops. Individuals.

Industry/Entity Type

Business

Contact Information for Business Card

Cells Q-Dash
Cars, Trucks, Boats, Motorcycles, lawn mowers, power tools
Delivery & install available most vehicles
Mon-Sat 9-6pm
Lyle Brockett 501-738-2054
*product warranty 6 month shelf life battery/1 year blems battery

```html
<!DOCTYPE html>
<html lang="en">
<head>
<meta charset="utf-8">
<title>Cells Q-Dash Business Card</title>
<link rel="stylesheet" href="https://fonts.googleapis.com/css2?family=Open+Sans:wght@400;600;700&display=swap">
<style>
  :root {
    --page: #f2efe9;
    --frame: #2b2b2b;
    --orange: #ff3d00;
    --denim: #3b5078;
    --white: #ffffff;
    --ink: #1a1a1a;
    --text-font: "Open Sans", Arial, sans-serif;
  }
  * { box-sizing: border-box; margin: 0; padding: 0; }
  html, body { width: 1200px; height: 819px; overflow: hidden; }
  body { background: var(--page); font-family: var(--text-font); color: var(--white); position: relative; }

  .card {
    position: absolute;
    border: 5px solid var(--frame);
    border-radius: 18px;
    overflow: hidden;
    background: var(--denim);
    box-shadow: inset 0 -6px 0 var(--orange), inset 6px 0 0 var(--orange), inset -6px 0 0 var(--orange);
  }
  .card-band { position: absolute; left: 0; right: 0; top: 0; background: var(--orange); }
  .mark-circle { position: absolute; border-radius: 50%; background: var(--white); }
  .brand-name { position: absolute; font-weight: 700; line-height: 1; color: var(--white); white-space: nowrap; }
  .tagline { position: absolute; font-size: 4.5px; font-weight: 600; color: var(--ink); white-space: nowrap; }
  .phone { position: absolute; display: flex; align-items: center; gap: 10px; font-weight: 400; white-space: nowrap; }
  .phone svg { display: block; }

  /* Front */
  .card-front { left: 228px; top: 146px; width: 368px; height: 200px; }
  .card-front .card-band { height: 102px; }
  .card-front .mark-circle { left: 32px; top: 50px; width: 92px; height: 92px; }
  .divider { position: absolute; left: 128px; top: 18px; width: 3px; height: 150px; background: var(--white); }
  .card-front .brand-name { left: 142px; top: 36px; font-size: 22px; }
  .card-front .tagline { left: 142px; top: 70px; }
  .person-name { position: absolute; left: 142px; top: 112px; font-size: 21px; font-weight: 400; }
  .card-front .phone { left: 197px; top: 156px; font-size: 16px; }

  /* Back */
  .card-back { left: 472px; top: 462px; width: 388px; height: 213px; }
  .card-back .card-band { height: 66px; }
  .card-back .mark-circle { left: 212px; top: 12px; width: 42px; height: 42px; }
  .card-back .brand-name { left: 262px; top: 20px; font-size: 13px; }
  .card-back .tagline { left: 262px; top: 40px; font-size: 3px; }
  .service-list { position: absolute; left: 34px; top: 70px; list-style: none; font-size: 7.5px; line-height: 9.8px; }
  .service-list li::before { content: "\25B8"; margin-right: 3px; }
  .info-line { position: absolute; left: 28px; font-size: 7.5px; }
  .info-delivery { top: 134px; }
  .info-hours { top: 148px; }
  .info-warranty { top: 162px; }
  .card-back .phone { left: 255px; top: 176px; font-size: 12px; gap: 8px; }
</style>
</head>
<body>
  <article class="card card-front">
    <div class="card-band"></div>
    <div class="mark-circle"></div>
    <div class="divider"></div>
    <div class="brand-name">Cells Q-Dash</div>
    <p class="tagline">Reconditioned / Used Batteries With Mobile Delivery And Install Services</p>
    <h1 class="person-name">Lyle Brockett</h1>
    <div class="phone">
      <svg width="18" height="18" viewBox="0 0 18 18" aria-hidden="true"><rect width="18" height="18" rx="3" fill="#fff"/><path d="M6 3.5c-1.2.4-2 1.3-2 2.6 0 3.8 3.6 8.4 7.5 8.4 1.1 0 1.9-.6 2.3-1.6l-2.2-1.7-1.3 1c-1.6-.8-3-2.6-3.5-4.2l1.2-1.1z" fill="#2b2b2b"/></svg>
      <span>501-738-2054</span>
    </div>
  </article>

  <article class="card card-back">
    <div class="card-band"></div>
    <div class="mark-circle"></div>
    <div class="brand-name">Cells Q-Dash</div>
    <p class="tagline">Reconditioned / Used Batteries With Mobile Delivery And Install Services</p>
    <ul class="service-list">
      <li>Cars</li>
      <li>Trucks</li>
      <li>Boats</li>
      <li>Motorcycles</li>
      <li>Lawn Mowers</li>
      <li>Power Tools</li>
    </ul>
    <p class="info-line info-delivery">Delivery &amp; install available most vehicles</p>
    <p class="info-line info-hours">Mon-Sat 9-6pm</p>
    <p class="info-line info-warranty">*product warranty 6 month shelf life battery/1 year blems battery</p>
    <div class="phone">
      <svg width="14" height="14" viewBox="0 0 18 18" aria-hidden="true"><rect width="18" height="18" rx="3" fill="#fff"/><path d="M6 3.5c-1.2.4-2 1.3-2 2.6 0 3.8 3.6 8.4 7.5 8.4 1.1 0 1.9-.6 2.3-1.6l-2.2-1.7-1.3 1c-1.6-.8-3-2.6-3.5-4.2l1.2-1.1z" fill="#2b2b2b"/></svg>
      <span>501-738-2054</span>
    </div>
  </article>
</body>
</html>
```